KJ Glimmer Cleaning Business Card

We need a business card for our new business, a cleaning company using steam. We already have a logo, and would like a modern-looking card using colors that go well with those in our logo.

```html
<!DOCTYPE html>
<html lang="en">
<head>
<meta charset="UTF-8">
<title>KJ Glimmer Cleaning Business Card</title>
<link href="https://fonts.googleapis.com/css2?family=Open+Sans:wght@400;600;800&display=swap" rel="stylesheet">
<style>
  :root {
    --page: #ececec;
    --card: #1f1f21;
    --card-back: #262628;
    --brand-blue: #2f73c9;
    --brand-blue-dim: #27507f;
    --accent-green: #22c04a;
    --texture-green: #2a3a26;
    --art-blue: #3f7fb8;
    --text-light: #f2f2f2;
    --text-soft: #cfcfcf;
  }
  * { box-sizing: border-box; margin: 0; padding: 0; }
  html, body { width: 1200px; height: 900px; overflow: hidden; }
  body {
    background: var(--page);
    font-family: "Open Sans", sans-serif;
    display: flex;
    align-items: center;
    justify-content: center;
    gap: 40px;
  }
  .card {
    position: relative;
    width: 540px;
    height: 310px;
    border-radius: 16px;
    overflow: hidden;
    box-shadow: 0 6px 18px rgba(0,0,0,0.25);
  }

  /* Back side */
  .card--back {
    background: var(--card-back);
    display: flex;
    align-items: center;
    justify-content: center;
    gap: 14px;
  }
  .card--back .brand-mark {
    width: 42px; height: 42px; border-radius: 50%;
    background: var(--brand-blue-dim);
    flex: none;
  }
  .card--back .brand-name {
    font-weight: 800;
    font-size: 36px;
    color: var(--brand-blue-dim);
    white-space: nowrap;
  }

  /* Front side */
  .card--front { background: var(--card); }
  .texture-area {
    position: absolute;
    right: 0; top: 60px;
    width: 330px; height: 110px;
    background: linear-gradient(90deg, rgba(42,58,38,0) 0%, var(--texture-green) 60%);
  }
  .brand-name--front {
    position: absolute;
    top: 18px; right: 26px;
    font-weight: 800;
    font-size: 30px;
    line-height: 1.2;
    color: var(--brand-blue);
    white-space: nowrap;
  }
  .art-area {
    position: absolute;
    right: 24px; top: 78px;
    width: 110px; height: 60px;
    border-radius: 4px;
    background: var(--art-blue);
  }
  .person { position: absolute; left: 28px; top: 70px; color: var(--text-light); }
  .person-name { font-size: 30px; font-weight: 600; line-height: 1.1; }
  .person-role { font-size: 13px; color: var(--text-soft); margin-top: 2px; }
  .phone { position: absolute; left: 28px; top: 128px; font-size: 12px; color: var(--text-light); }
  .address { position: absolute; left: 150px; top: 150px; font-size: 13px; color: var(--text-light); }
  .email { position: absolute; right: 28px; top: 154px; font-size: 12px; color: var(--text-light); }
  .divider {
    position: absolute; left: 150px; right: 24px; top: 176px;
    height: 2px; background: var(--accent-green);
  }
  .web-list {
    position: absolute; left: 120px; top: 190px;
    list-style: none; font-size: 13px; color: var(--text-light); line-height: 1.6;
  }
</style>
</head>
<body>
  <section class="card card--back" aria-label="Business card back">
    <span class="brand-mark"></span>
    <span class="brand-name">KJ Glimmer Cleaning</span>
  </section>

  <section class="card card--front" aria-label="Business card front">
    <div class="texture-area" role="img" aria-label="Decorative green pattern area"></div>
    <div class="brand-name--front">KJ Glimmer Cleaning</div>
    <div class="art-area" role="img" aria-label="Water drop illustration area"></div>

    <div class="person">
      <div class="person-name">Name</div>
      <div class="person-role">Designation</div>
    </div>
    <div class="phone">Phone:01-999-999-99</div>
    <div class="address">Address</div>
    <div class="email">Email:something@example.com</div>
    <div class="divider"></div>
    <ul class="web-list">
      <li>web:www.example.com</li>
      <li>web:www.example.com</li>
      <li>web:www.example.com</li>
      <li>web:www.example.com</li>
    </ul>
  </section>
</body>
</html>
```